Business Card for Amber Finch Advisors

Business card design for Amber Finch Advisors, a new consulting and financial advisory firm. I would like the designs to integrate the logo attached (at least on 1 side).

Target Market(s)

individual and institutional clients

Contact Information for Business Card

Daniel R. Hollis, CFA
Managing Director
amberfinchadvisors.comp
hollis@amberfinchadvisors.example
(555) 217-4630

```html
<!DOCTYPE html>
<html lang="en">
<head>
<meta charset="utf-8">
<title>Amber Finch Advisors — Business Card</title>
<link rel="stylesheet" href="https://fonts.googleapis.com/css2?family=Jost:wght@400;500&family=League+Spartan:wght@700&display=swap">
<style>
  :root {
    --backdrop: #222222;
    --card: #1e2124;
    --amber: #e08a1e;
    --ink-light: #f2f2f2;
  }
  * { box-sizing: border-box; margin: 0; padding: 0; }
  html, body {
    width: 1189px;
    height: 1200px;
    overflow: hidden;
    background: var(--backdrop);
  }
  .sheet {
    position: relative;
    width: 1189px;
    height: 1200px;
  }
  .card {
    position: absolute;
    left: 167px;
    width: 855px;
    height: 488px;
    background: var(--card);
    display: flex;
    flex-direction: column;
    align-items: center;
    justify-content: center;
    text-align: center;
  }
  .card--front { top: 67px; }
  .card--back { top: 626px; justify-content: flex-start; }

  .brand-name {
    font-family: "Jost", sans-serif;
    font-weight: 500;
    font-size: 46px;
    letter-spacing: 1px;
    color: var(--amber);
    text-transform: uppercase;
  }

  .holder-name {
    margin-top: 144px;
    font-family: "League Spartan", sans-serif;
    font-weight: 700;
    font-size: 28px;
    letter-spacing: 0.5px;
    color: var(--amber);
    line-height: 1;
  }
  .holder-title {
    margin-top: 8px;
    font-family: "Jost", sans-serif;
    font-weight: 400;
    font-size: 19px;
    letter-spacing: 0.5px;
    color: var(--ink-light);
  }
  .contact-list {
    list-style: none;
    margin-top: 74px;
    font-family: "Jost", sans-serif;
    font-weight: 400;
    font-size: 19px;
    letter-spacing: 0.5px;
    color: var(--ink-light);
    line-height: 30px;
  }
  .contact-list .web { margin-top: 7px; }
  .contact-list .web-domain { color: var(--amber); }
</style>
</head>
<body>
  <main class="sheet">
    <section class="card card--front" aria-label="Card front">
      <h1 class="brand-name">Amber Finch Advisors</h1>
    </section>

    <section class="card card--back" aria-label="Card back">
      <h2 class="holder-name">DANIEL R. HOLLIS, CFA</h2>
      <p class="holder-title">Managing Director</p>
      <ul class="contact-list">
        <li class="phone">(555) 217-4630</li>
        <li class="email">hollis@amberfinchadvisors.example</li>
        <li class="web"><span class="web-domain">amberfinchadvisors</span>.comp</li>
      </ul>
    </section>
  </main>
</body>
</html>
```